Business card design for Plumbing and Gas fitting company

We need a business card design for our plumbing and gas fitting company using the company logo and director details. Design should be modern and eye-catching however kept reasonably simple. This design should be targeted at commercial businesses/work so professionalism is key.

Target Market(s)

Commercial/business

Industry/Entity Type

Plumbing

Contact Information for Business Card

Warren Dohey
Director
027 581 9043
warren@vantorplumbingandgas.example
PO Box 7816
Palmerston North 4472

Font styles to use
Sans Serif

Requirements
Must have
• Logo
• Modern
• Kept simple
Nice to have
• Colour scheme based around logo

```html
<!DOCTYPE html>
<html lang="en">
<head>
<meta charset="utf-8">
<title>Vantor Plumbing &amp; Gas – Business Card</title>
<link rel="stylesheet" href="https://fonts.googleapis.com/css2?family=Montserrat:wght@400;500;700&display=swap">
<style>
  :root {
    --bg: #ecebf4;
    --card: #f7f7f8;
    --grey: #7b7c7d;
    --grey-dark: #6a6b6c;
    --orange: #e8642c;
    --blue: #1d74c4;
    --white: #ffffff;
  }
  * { box-sizing: border-box; margin: 0; padding: 0; }
  html, body {
    width: 1200px; height: 900px; overflow: hidden;
    background: var(--bg);
    font-family: "Montserrat", sans-serif;
  }
  .canvas {
    position: relative; width: 1200px; height: 900px;
    display: flex; flex-direction: column; align-items: center; justify-content: center; gap: 48px;
  }
  .card {
    position: relative; width: 630px; height: 360px;
    background: var(--card); border-radius: 22px; overflow: hidden;
    box-shadow: 0 10px 30px rgba(60, 60, 90, 0.18);
  }
  /* Front */
  .card-front { display: flex; align-items: center; justify-content: center; }
  .brand { display: flex; align-items: center; gap: 16px; }
  .brand-name { font-weight: 700; color: var(--grey); }
  .brand-dot { border-radius: 50%; background: var(--orange); flex: none; }
  .card-front .brand-name { font-size: 38px; letter-spacing: 0.5px; }
  .card-front .brand-dot { width: 34px; height: 34px; }
  /* Back */
  .card-back .band { position: absolute; inset: 0; width: 100%; height: 100%; }
  .details {
    position: absolute; left: 40px; top: 52px; color: var(--white);
  }
  .details .name { font-size: 30px; font-weight: 700; letter-spacing: 1px; margin-bottom: 8px; }
  .details .role { font-size: 15px; font-weight: 500; margin-bottom: 10px; }
  .details .line { font-size: 15px; font-weight: 500; line-height: 1.5; }
  .card-back .brand { position: absolute; right: 34px; bottom: 36px; gap: 10px; }
  .card-back .brand-name { font-size: 20px; }
  .card-back .brand-dot { width: 18px; height: 18px; }
</style>
</head>
<body>
<main class="canvas">
  <section class="card card-front" aria-label="Card front">
    <div class="brand">
      <span class="brand-name">Vantor Plumbing &amp; Gas</span>
      <span class="brand-dot"></span>
    </div>
  </section>

  <section class="card card-back" aria-label="Card back">
    <svg class="band" viewBox="0 0 630 360" preserveAspectRatio="none" aria-hidden="true">
      <line x1="0" y1="22" x2="630" y2="22" stroke="var(--orange)" stroke-width="2"/>
      <path d="M0 34 H520 V150 C520 190 495 200 460 205 C410 212 395 230 385 270 H0 Z" fill="var(--grey)"/>
    </svg>
    <div class="details">
      <p class="name">Warren Dohey</p>
      <p class="role">Director</p>
      <p class="line">027 581 9043</p>
      <p class="line">warren@vantorplumbingandgas.example</p>
      <p class="line">PO Box 7816</p>
      <p class="line">Palmerston North 4472</p>
    </div>
    <div class="brand">
      <span class="brand-name">Vantor Plumbing &amp; Gas</span>
      <span class="brand-dot"></span>
    </div>
  </section>
</main>
</body>
</html>
```